K&B RESTORATION

I want a brochure similiar to the example i've attached.
My company name is K&B Restoration. The website is: K-B-Restoration.com.
The phone number is 404.555.0173.

I don't like the "yellow" being the main color of the example so I'm open to suggestions. I want something CLEAN & Simple, like our logo . This will be a bi fold brochure

```html
<!DOCTYPE html>
<html lang="en">
<head>
<meta charset="UTF-8">
<title>K&amp;B Restoration – Insurance Claim Specialist</title>
<link href="https://fonts.googleapis.com/css2?family=Poppins:wght@400;500&display=swap" rel="stylesheet">
<style>
  :root {
    --ink: #1f1f1f;
    --charcoal: #4d4d4d;
    --green: #87b833;
    --green-light: #aedb5e;
    --green-deep: #6f9a28;
    --paper: #ffffff;
  }
  html, body {
    margin: 0;
    padding: 0;
    overflow: hidden;
    background: var(--paper);
  }
  .brochure-cover {
    position: relative;
    width: 848px;
    height: 1200px;
    overflow: hidden;
    background: var(--paper);
    font-family: "Poppins", sans-serif;
  }
  .cover-shapes {
    position: absolute;
    inset: 0;
    width: 848px;
    height: 1200px;
  }
  .brand-name {
    position: absolute;
    left: 352px;
    top: 150px;
    width: 340px;
    margin: 0;
    text-align: center;
    font-weight: 500;
    font-size: 40px;
    letter-spacing: 1px;
    color: var(--ink);
    line-height: 1;
  }
  .headline {
    margin: 0;
  }
  .headline-line {
    position: absolute;
    display: block;
    color: var(--paper);
    font-weight: 500;
    line-height: 1;
    white-space: nowrap;
    transform-origin: 0 0;
    transform: rotate(27deg);
  }
  .headline-line--insurance {
    left: 276px;
    top: 296px;
    font-size: 92px;
    letter-spacing: 1px;
  }
  .headline-line--claim {
    left: 232px;
    top: 372px;
    font-size: 150px;
  }
  .headline-line--specialist {
    left: 178px;
    top: 492px;
    font-size: 88px;
  }
  .website {
    position: absolute;
    left: 384px;
    top: 1117px;
    display: flex;
    align-items: center;
    gap: 10px;
    color: var(--ink);
    font-weight: 500;
    font-size: 31px;
    line-height: 1;
  }
  .website-icon {
    width: 32px;
    height: 32px;
    flex: none;
  }
</style>
</head>
<body>
  <main class="brochure-cover">
    <svg class="cover-shapes" viewBox="0 0 1623 2296" preserveAspectRatio="none" aria-hidden="true">
      <defs>
        <linearGradient id="photoTone" x1="0" y1="0" x2="1" y2="1">
          <stop offset="0" stop-color="#b6e36a"/>
          <stop offset="0.6" stop-color="#9ccd4c"/>
          <stop offset="1" stop-color="#7aa534"/>
        </linearGradient>
      </defs>
      <polygon class="charcoal-wedge" points="0,0 605,0 0,1160" fill="var(--charcoal)"/>
    </svg>
    <svg class="cover-shapes" viewBox="0 0 1623 2296" preserveAspectRatio="none" role="img" aria-label="Photo of a kitchen under renovation with new cabinets, tinted green">
      <polygon class="photo-panel" points="390,415 0,1160 0,2296 460,2296 870,1515" fill="url(#photoTone)"/>
    </svg>
    <svg class="cover-shapes" viewBox="0 0 1623 2296" preserveAspectRatio="none" aria-hidden="true">
      <polygon class="green-band" points="390,415 1623,1045 1623,1900 0,1071 0,1160" fill="var(--green)" opacity="0.92"/>
    </svg>

    <p class="brand-name">K&amp;B Restoration</p>

    <h1 class="headline">
      <span class="headline-line headline-line--insurance">INSURANCE</span>
      <span class="headline-line headline-line--claim">CLAIM</span>
      <span class="headline-line headline-line--specialist">SPECIALIST</span>
    </h1>

    <div class="website">
      <svg class="website-icon" viewBox="0 0 32 32" aria-hidden="true">
        <circle cx="16" cy="16" r="15" fill="var(--green)"/>
        <ellipse cx="16" cy="16" rx="6" ry="15" fill="none" stroke="var(--paper)" stroke-width="1.6"/>
        <line x1="1" y1="16" x2="31" y2="16" stroke="var(--paper)" stroke-width="1.6"/>
        <line x1="16" y1="1" x2="16" y2="31" stroke="var(--paper)" stroke-width="1.6"/>
      </svg>
      <span class="website-url">K-B-Restoration.com</span>
    </div>
  </main>
</body>
</html>
```